Etiketten für Kuchen im Glas
Zielgruppe
Die Firma Brelkat bietet kulinarische Präsente und Geschenkideen zum Thema kreatives Backen an. Unsere Zielgruppe ist B2C und Werbetreibende, die unsere Produkte als Geschenke einsetzen.
Aufgabenstellung
Für unsere Zielgruppe "Feinkostläden" benötigen wir ein etwas edleres klasssisches Etiketten-Design.
Gestaltet wird der Deckel und die Vorderseite eines Etiketts für ein 290 ml FUMS-Glas. Die entsprechende Designvorlage steht hier zum Download bereit:
https://files.tralvex-speicher.de/u/4827351/7902_01358_0000-Vorlage%20CMYK%20v08_2013-09.psd
Benötigt werden 4 unterschiedliche Etiketten, die aber aus einem "Guss" sein sollten für die Sorten: Stracciatella, Schokolade, Zitrone, Stollen. Die Sorte sollte mit auf dem Etikett stehen.
Sonstige Angaben auf dem Etikett:
- optional "Kuchen im Glas"
- gerne Grünhof Logo (siehe Anhang)
- optional "fertig gebacken". Könnte z.B. gut auf dem Deckel in Kombination mit "Kuchen im Gla" stehen
Achtung: Das Etikett für die Rückseite mit Deklaration muss nicht gestaltet werden.
Tipps: Das Etikett ist konisch und das Glas rund. Das bedeutet, dass Bilder + Schriften mit einer leichten Wölbung kreiert werden sollten. Für die Wölbung kann man sich gut an der unteren Designlinie orientieren.
Farbgestaltung: eher dunkel; z.B. Grau, Dunkelblau evtl. Schwarz
Schriften: Es dürfen auch kostenpflichtige Schriften verwendet werden. Freie Schriften allerdings bevorzugt
Format: Photoshop PSD inklusive allen Ebenen und verwendeten Elementen als einzelne Ebene.
Bei Fragen gerne melden, ich freue mich auf Eure Designs.

```html
<!DOCTYPE html>
<html lang="de">
<head>
<meta charset="utf-8">
<title>Kuchen im Glas – Etiketten Zitrone</title>
<link rel="stylesheet" href="https://fonts.googleapis.com/css2?family=Marcellus&family=Pinyon+Script&family=Dancing+Script:wght@500&display=swap">
<style>
  :root {
    --frame-grey: #8a8a8a;
    --page-white: #ffffff;
    --label-black: #1c1c1c;
    --label-dark: #262626;
    --label-mid: #3a3a3a;
    --badge-cream: #f7f5ee;
    --badge-edge: #ddd8c8;
    --ribbon-cream: #f8f5e9;
    --ribbon-shade: #c9c3b0;
    --ink: #151515;
    --caption-white: #f2f2f2;
    --lemon-yellow: #f3cf2a;
    --leaf-green: #3f8a2e;
    --divider: #9a9482;
  }
  html, body {
    margin: 0;
    padding: 0;
    width: 1200px;
    height: 421px;
    overflow: hidden;
    background: var(--page-white);
  }
  .label-sheet { display: block; width: 1200px; height: 421px; }
  .caption-top {
    font-family: "Marcellus", serif;
    fill: var(--caption-white);
    letter-spacing: 1px;
  }
  .product-title {
    font-family: "Pinyon Script", cursive;
    fill: var(--ink);
  }
  .flavour-name {
    font-family: "Dancing Script", cursive;
    font-weight: 500;
    fill: var(--ink);
  }
  .certifier-name {
    font-family: "Marcellus", serif;
    fill: var(--caption-white);
  }
</style>
</head>
<body>
<svg class="label-sheet" viewBox="0 0 1200 421" xmlns="http://www.w3.org/2000/svg">
  <defs>
    <radialGradient id="label-surface" cx="50%" cy="45%" r="65%">
      <stop offset="0" stop-color="var(--label-mid)"/>
      <stop offset="0.6" stop-color="var(--label-dark)"/>
      <stop offset="1" stop-color="var(--label-black)"/>
    </radialGradient>
    <radialGradient id="badge-fill" cx="50%" cy="45%" r="55%">
      <stop offset="0" stop-color="#ffffff"/>
      <stop offset="1" stop-color="var(--badge-cream)"/>
    </radialGradient>
    <radialGradient id="lemon-fill" cx="50%" cy="50%" r="50%">
      <stop offset="0" stop-color="#fbe98a"/>
      <stop offset="0.7" stop-color="var(--lemon-yellow)"/>
      <stop offset="1" stop-color="var(--leaf-green)"/>
    </radialGradient>
    <filter id="title-glow" x="-20%" y="-40%" width="140%" height="180%">
      <feGaussianBlur in="SourceAlpha" stdDeviation="4" result="blur"/>
      <feFlood flood-color="#ffffff" flood-opacity="0.95"/>
      <feComposite in2="blur" operator="in" result="glow"/>
      <feMerge><feMergeNode in="glow"/><feMergeNode in="glow"/><feMergeNode in="SourceGraphic"/></feMerge>
    </filter>
    <filter id="soft-drop" x="-10%" y="-10%" width="120%" height="130%">
      <feDropShadow dx="0" dy="2" stdDeviation="2" flood-color="#000" flood-opacity="0.45"/>
    </filter>
  </defs>

  <rect class="sheet-frame" x="3" y="3" width="1194" height="415" fill="var(--page-white)" stroke="var(--frame-grey)" stroke-width="6"/>

  <g class="lid-label">
    <circle cx="217" cy="206" r="186" fill="url(#label-surface)"/>
    <text class="caption-top" x="217" y="75" text-anchor="middle" font-size="16">- FERTIG GEBACKEN -</text>
    <g class="lid-badge" filter="url(#soft-drop)">
      <circle cx="217" cy="212" r="104" fill="var(--badge-edge)"/>
      <circle cx="217" cy="212" r="97" fill="url(#badge-fill)" stroke="#cfc9b6" stroke-width="1"/>
    </g>
    <ellipse cx="217" cy="150" rx="34" ry="22" fill="url(#lemon-fill)" role="img" aria-label="Zitronen mit Blättern"/>
    <text class="product-title" x="217" y="218" text-anchor="middle" font-size="50" filter="url(#title-glow)" textLength="290">Kuchen im Glas</text>
    <g class="flavour-ribbon" filter="url(#soft-drop)">
      <path d="M102 246 Q217 240 332 246 L328 274 Q217 268 106 274 Z" fill="var(--ribbon-cream)" stroke="var(--ribbon-shade)" stroke-width="0.8"/>
    </g>
    <text class="flavour-name" x="217" y="266" text-anchor="middle" font-size="22">Zitrone</text>
    <g class="badge-divider" stroke="var(--divider)" stroke-width="1">
      <line x1="190" y1="292" x2="212" y2="292"/>
      <line x1="222" y1="292" x2="244" y2="292"/>
    </g>
    <circle cx="217" cy="292" r="2" fill="var(--divider)"/>
  </g>

  <g class="front-label">
    <path d="M466 69 Q815 50 1165 69 Q1185 70 1183 90 L1136 364 Q1133 385 1114 384 Q815 340 516 384 Q497 385 494 364 L447 90 Q445 70 466 69 Z" fill="url(#label-surface)"/>
    <text class="caption-top" x="815" y="84" text-anchor="middle" font-size="19">- FERTIG GEBACKEN -</text>
    <g class="front-badge" filter="url(#soft-drop)">
      <circle cx="815" cy="212" r="118" fill="var(--badge-edge)"/>
      <circle cx="815" cy="212" r="110" fill="url(#badge-fill)" stroke="#cfc9b6" stroke-width="1"/>
    </g>
    <ellipse cx="815" cy="154" rx="40" ry="26" fill="url(#lemon-fill)" role="img" aria-label="Zitronen mit Blättern"/>
    <text class="product-title" x="815" y="228" text-anchor="middle" font-size="58" filter="url(#title-glow)" textLength="312">Kuchen im Glas</text>
    <g class="flavour-ribbon" filter="url(#soft-drop)">
      <path d="M696 255 Q815 248 935 255 L931 287 Q815 280 700 287 Z" fill="var(--ribbon-cream)" stroke="var(--ribbon-shade)" stroke-width="0.8"/>
    </g>
    <text class="flavour-name" x="815" y="279" text-anchor="middle" font-size="24">Zitrone</text>
    <g class="badge-divider" stroke="var(--divider)" stroke-width="1">
      <line x1="785" y1="300" x2="810" y2="300"/>
      <line x1="820" y1="300" x2="845" y2="300"/>
    </g>
    <circle cx="815" cy="300" r="2" fill="var(--divider)"/>
    <text class="certifier-name" x="505" y="335" font-size="17">Grünhof</text>
  </g>
</svg>
</body>
</html>
```